Torvane Travel Business Card Design

We need a new business card design for our travel agency business - Torvane Travel. We design packages to some of the most popular travel destinations in the world for groups, individuals and also tailor-make personalised packages. Our logo attached must be used. On the back of the card we would like a list of all websites under our Torvane brand to be posted. We would like clean, modern, simple design.

Industry/Entity Type

Travel Agent

Contact Information for Business Card

Owen Pridmore
National Sales Manager
Reservations: 1300 742 689
Tel: 61 28473 5096
Fax: 61 2847 3971
Email: owen@torvanetravel.com.au
Web: www.torvanetravel.com.au

Address: Level 1, 417 Harwick Street
Sydney NSW 2000 Australia

Requirements
Must have
• On the back of the card we want all websites listed under our Torvane brand.
• Torvane Travel Group - Wholesale Specialists
• www.qpjourneys.com.au - New Caledonia
• www.bravelmijourneys.com.au - Tahiti
• www.sorvenbreakhub.com.au - China
Nice to have
• Modern, clean lined, simple and fresh
Should not have
• Look dull

```html
<!DOCTYPE html>
<html lang="en">
<head>
<meta charset="utf-8">
<title>Torvane Travel Business Card</title>
<link rel="stylesheet" href="https://fonts.googleapis.com/css2?family=Fira+Sans+Condensed:wght@500&family=Source+Sans+3:wght@400&display=swap">
<style>
  :root {
    --navy: #2e2a7e;
    --red: #e0312b;
    --paper: #ffffff;
    --rule: #e3e3e6;
    --backdrop: #a9a7a8;
    --decor: #f1f1f3;
  }
  * { margin: 0; padding: 0; box-sizing: border-box; }
  html, body { width: 1200px; height: 1200px; overflow: hidden; }
  body {
    background: var(--backdrop);
    position: relative;
    font-family: "Source Sans 3", sans-serif;
    color: var(--navy);
  }
  .card {
    position: absolute;
    left: 244px;
    width: 712px;
    height: 420px;
    background: var(--paper);
    border-radius: 24px;
    overflow: hidden;
  }
  .card--back { top: 118px; }
  .card--front { top: 644px; }
  .decor {
    position: absolute;
    background: radial-gradient(ellipse at center, var(--decor) 0%, var(--decor) 45%, rgba(241,241,243,0) 72%);
  }
  .brand-name {
    position: absolute;
    font-family: "Fira Sans Condensed", sans-serif;
    font-weight: 500;
    line-height: 1;
    color: var(--navy);
    white-space: nowrap;
  }
  .card--back .brand-name {
    left: 0; right: 0; top: 118px;
    text-align: center;
    font-size: 48px;
  }
  .strapline {
    position: absolute;
    left: 0; right: 0; top: 190px;
    text-align: center;
    font-size: 19px;
    letter-spacing: .58em;
    padding-left: .58em;
    color: var(--navy);
  }
  .site-list {
    position: absolute;
    left: 0; right: 0; top: 268px;
    list-style: none;
    text-align: center;
    font-size: 18px;
    line-height: 24px;
  }
  .site-list a, .accent { color: var(--red); text-decoration: none; }
  .band { position: absolute; left: 0; bottom: 0; width: 712px; }
  .card--front .brand-name {
    left: 36px; width: 314px; top: 176px;
    text-align: center;
    font-size: 50px;
  }
  .divider {
    position: absolute;
    left: 377px; top: 56px;
    width: 1px; height: 260px;
    background: var(--rule);
  }
  .contact { position: absolute; left: 413px; top: 62px; }
  .contact-name {
    font-family: "Fira Sans Condensed", sans-serif;
    font-weight: 500;
    font-size: 28px;
    line-height: 34px;
    color: var(--navy);
  }
  .contact-role { font-size: 17px; color: var(--red); margin-top: 6px; }
  .contact-lines { list-style: none; margin-top: 28px; font-size: 18px; line-height: 24px; }
  .contact-lines li { display: flex; align-items: center; }
  .contact-lines svg { width: 16px; height: 16px; margin-right: 20px; fill: var(--red); }
  .address { font-size: 18px; line-height: 27px; margin-top: 4px; }
  .reservations {
    position: absolute;
    left: 413px; top: 380px;
    font-size: 18px;
    line-height: 24px;
    color: #fff;
  }
</style>
</head>
<body>

<section class="card card--back">
  <div class="decor" role="img" aria-label="faint aircraft silhouette in the background" style="left:10px;top:40px;width:660px;height:340px;"></div>
  <div class="brand-name">Torvane Travel Group</div>
  <p class="strapline">Wholesale Specialists</p>
  <ul class="site-list">
    <li>New Caledonia - <a href="#">www.qpjourneys.com.au</a></li>
    <li>Tahiti - <a href="#">www.bravelmijourneys.com.au</a></li>
    <li>China - <a href="#">www.sorvenbreakhub.com.au</a></li>
  </ul>
  <svg class="band" viewBox="0 0 712 18" height="18" aria-hidden="true">
    <polygon points="0,0 503,0 462,18 0,18" fill="var(--red)"/>
    <polygon points="510,0 712,0 712,18 470,18" fill="var(--navy)"/>
  </svg>
</section>

<section class="card card--front">
  <div class="decor" role="img" aria-label="faint aircraft silhouette in the background" style="left:260px;top:20px;width:460px;height:340px;"></div>
  <div class="brand-name">Torvane Travel</div>
  <div class="divider"></div>
  <div class="contact">
    <h1 class="contact-name">Owen Pridmore</h1>
    <p class="contact-role">National Sales Manager</p>
    <ul class="contact-lines">
      <li><svg viewBox="0 0 16 16"><path d="M2 6c0-2 2-3 6-3s6 1 6 3v1h-3V6H5v1H2zM4 8h8l2 5H2z"/></svg>61 28473 5096</li>
      <li><svg viewBox="0 0 16 16"><path d="M4 1h8v4H4zM1 6h14v6h-3v3H4v-3H1zM5 10v4h6v-4z"/></svg>61 2847 3971</li>
      <li><svg viewBox="0 0 16 16"><path d="M1 3h14v10H1zM2.5 4.5 8 9l5.5-4.5v-.2H2.5z" fill-rule="evenodd"/></svg>owen@torvanetravel.com.au</li>
      <li><svg viewBox="0 0 16 16"><path d="M8 1a7 7 0 1 0 0 14A7 7 0 0 0 8 1zm0 1.5c.8 0 1.7 1.6 2 4H6c.3-2.4 1.2-4 2-4zM2.6 6.5h2c-.1.5-.1 1-.1 1.5s0 1 .1 1.5h-2a5.6 5.6 0 0 1 0-3zm3.4 0h4c.1.5.1 1 .1 1.5s0 1-.1 1.5H6c-.1-.5-.1-1-.1-1.5s0-1 .1-1.5zm5.4 0h2a5.6 5.6 0 0 1 0 3h-2c.1-.5.1-1 .1-1.5s0-1-.1-1.5zM6 11h4c-.3 1.9-1.2 3.5-2 3.5S6.3 12.9 6 11z"/></svg>www.torvane<span class="accent">travel</span>.com.au</li>
    </ul>
    <p class="address">Level 1, 417 Harwick Street<br>Sydney NSW 2000 Australia</p>
  </div>
  <svg class="band" viewBox="0 0 712 56" height="56" aria-hidden="true">
    <polygon points="0,28 370,28 357,56 0,56" fill="var(--navy)"/>
    <polygon points="380,0 712,0 712,56 353,56" fill="var(--red)"/>
  </svg>
  <p class="reservations">Reservations: 1300 742 689</p>
</section>

</body>
</html>
```